Meadowlark Counseling Business Card Design Project

I am starting a new business that provides counseling and coaching services to individuals and couples. These individuals are people looking to "transform" or grow in the personal lives. The design should convey trust, intimacy, hope, growth. It should be professional, elegant.
Contact information
Name: Dana R. Whitcombe
Title: Counselor and Life Coach
Slogan: Bringing Hope. Transforming Lives.
address: 47310 County Road 9, Suite 410
Plymouth, MN 55490
Phone: 763-555-0184
Email: dana@meadowlark-cx.example
website: www.meadowlark-cx.example
Back side of card should have bullets:
Individual counseling
Relationship counseling
Life Coaching for Teens and Adults
Group Workshops

```html
<!DOCTYPE html>
<html lang="en">
<head>
<meta charset="utf-8">
<title>Meadowlark Counseling – Business Card Set</title>
<link rel="stylesheet" href="https://fonts.googleapis.com/css2?family=Crimson+Text:ital,wght@0,400;1,400&display=swap">
<style>
  :root {
    --page: #ffffff;
    --frame: #2b2b2b;
    --ink-grey: #858585;
    --ink-dark: #2a2f3a;
    --ink-light: #eef1f6;
    --rule-light: #c9c9c9;
    --navy: #16224b;
    --navy-mid: #1c3a6e;
    --sky: #2a93cc;
    --steel-dark: #5e5e5e;
    --steel-mid: #8c8c8c;
    --steel-light: #e6e6e6;
    --brand-blue: #1f6fa8;
  }
  * { margin: 0; padding: 0; box-sizing: border-box; }
  html, body { width: 1200px; height: 1000px; overflow: hidden; background: var(--page); }
  body { position: relative; font-family: "Crimson Text", Georgia, serif; }

  .card {
    position: absolute;
    width: 323px;
    height: 185px;
    border: 1px solid var(--frame);
    overflow: hidden;
  }
  .card--front { left: 262px; }
  .card--back  { left: 615px; }
  .row-1 { top: 225px; }
  .row-2 { top: 422px; }
  .row-3 { top: 619px; }

  .card--white { background: #ffffff; }
  .card--navy.card--front {
    background: linear-gradient(90deg, var(--navy) 0%, var(--navy) 28%, var(--navy-mid) 50%, var(--sky) 75%, var(--navy-mid) 92%, var(--navy) 100%);
  }
  .card--navy.card--back {
    background: linear-gradient(90deg, var(--sky) 0%, #2478b0 18%, var(--navy-mid) 45%, var(--navy) 62%, var(--navy) 100%);
  }
  .card--steel.card--front {
    background: linear-gradient(90deg, var(--steel-dark) 0%, var(--steel-dark) 28%, var(--steel-mid) 55%, #cfcfcf 82%, var(--steel-mid) 100%);
  }
  .card--steel.card--back {
    background: linear-gradient(90deg, var(--steel-light) 0%, #cdcdcd 30%, #a8a8a8 60%, #9a9a9a 100%);
  }

  /* Front */
  .holder-name {
    position: absolute; left: 38px; top: 44px;
    font-size: 21px; font-weight: 400; letter-spacing: 0.3px; line-height: 1;
  }
  .holder-title {
    position: absolute; left: 39px; top: 70px;
    font-size: 10.5px; font-style: italic; letter-spacing: 0.3px;
  }
  .address {
    position: absolute; left: 50px; top: 95px;
    font-size: 10.5px; line-height: 16px;
  }
  .contact-rule {
    position: absolute; left: 20px; right: 18px; top: 165px;
    height: 1px;
  }
  .contact-line {
    position: absolute; left: 37px; top: 168px;
    font-size: 10px; white-space: nowrap;
  }
  .contact-line .sep { margin: 0 6px; }

  .card--white .holder-name,
  .card--white .holder-title,
  .card--white .address,
  .card--white .contact-line { color: var(--ink-grey); }
  .card--white .contact-rule { background: var(--rule-light); }
  .card--navy .holder-name,
  .card--navy .holder-title,
  .card--navy .address,
  .card--navy .contact-line,
  .card--steel .holder-name,
  .card--steel .holder-title,
  .card--steel .address,
  .card--steel .contact-line { color: var(--ink-light); }
  .card--steel .contact-line,
  .card--steel .address { text-shadow: 0 0 2px rgba(0,0,0,0.55); }
  .card--navy .contact-rule,
  .card--steel .contact-rule { background: rgba(255,255,255,0.55); }

  .emblem-area {
    position: absolute; left: 222px; top: 16px;
    width: 88px; height: 140px;
    border-radius: 50%;
    background: radial-gradient(ellipse at center, rgba(190,200,215,0.4) 0%, rgba(190,200,215,0) 70%);
  }

  /* Back */
  .brand {
    position: absolute; left: 22px; top: 24px;
    display: flex; align-items: center; gap: 12px;
  }
  .brand-dot { width: 30px; height: 30px; border-radius: 50%; background: var(--brand-blue); flex: none; }
  .brand-name { color: var(--brand-blue); font-weight: 400; line-height: 1; }
  .brand-name .primary { display: block; font-size: 24px; letter-spacing: 0.5px; }
  .brand-name .secondary { display: block; font-size: 9.5px; letter-spacing: 2.4px; margin-top: 4px; }

  .slogan {
    position: absolute; left: 0; right: 0; top: 78px;
    text-align: center; font-size: 11.5px; font-style: italic;
  }
  .services {
    position: absolute; left: 30px; right: 16px; top: 102px;
    list-style: none;
    display: grid; grid-template-columns: 1fr 1.25fr; row-gap: 3px; column-gap: 8px;
    font-size: 10px; line-height: 13px;
  }
  .services li::before { content: "•"; margin-right: 5px; }

  .website {
    position: absolute; right: 4px; bottom: 2px;
    font-size: 10px;
  }

  .card--white .slogan,
  .card--white .services { color: var(--ink-dark); }
  .card--white .website { color: var(--ink-grey); }

  .card--navy .brand-name,
  .card--navy .slogan,
  .card--navy .services,
  .card--navy .website { color: var(--ink-light); }
  .card--navy .brand-dot { background: var(--ink-light); }

  .card--steel .brand-name { color: var(--navy-mid); }
  .card--steel .brand-dot { background: var(--navy-mid); }
  .card--steel .slogan,
  .card--steel .services,
  .card--steel .website { color: #1e2330; }
</style>
</head>
<body>

  <!-- White set -->
  <section class="card card--front card--white row-1">
    <div class="emblem-area" role="img" aria-label="Faint brand emblem decoration"></div>
    <h1 class="holder-name">Dana R. Whitcombe</h1>
    <p class="holder-title">Counselor and Life Coach</p>
    <p class="address">47310 County Road 9, Suite 410<br>Plymouth, MN 55490</p>
    <div class="contact-rule"></div>
    <p class="contact-line">Contact -<span class="sep"></span>763-555-0184<span class="sep">-</span>dana@meadowlark-cx.example</p>
  </section>
  <section class="card card--back card--white row-1">
    <div class="brand">
      <span class="brand-dot"></span>
      <p class="brand-name"><span class="primary">MEADOWLARK</span><span class="secondary">COUNSELING AND COACHING</span></p>
    </div>
    <p class="slogan">Bringing Hope. Transforming Lives.</p>
    <ul class="services">
      <li>Individual counseling</li>
      <li>Relationship counseling</li>
      <li>Group Workshops</li>
      <li>Life Coaching for Teens and Adults</li>
    </ul>
    <p class="website">www.meadowlark-cx.example</p>
  </section>

  <!-- Navy set -->
  <section class="card card--front card--navy row-2">
    <div class="emblem-area" role="img" aria-label="Faint brand emblem decoration"></div>
    <h1 class="holder-name">Dana R. Whitcombe</h1>
    <p class="holder-title">Counselor and Life Coach</p>
    <p class="address">47310 County Road 9, Suite 410<br>Plymouth, MN 55490</p>
    <div class="contact-rule"></div>
    <p class="contact-line">Contact -<span class="sep"></span>763-555-0184<span class="sep">-</span>dana@meadowlark-cx.example</p>
  </section>
  <section class="card card--back card--navy row-2">
    <div class="brand">
      <span class="brand-dot"></span>
      <p class="brand-name"><span class="primary">MEADOWLARK</span><span class="secondary">COUNSELING AND COACHING</span></p>
    </div>
    <p class="slogan">Bringing Hope. Transforming Lives.</p>
    <ul class="services">
      <li>Individual counseling</li>
      <li>Relationship counseling</li>
      <li>Group Workshops</li>
      <li>Life Coaching for Teens and Adults</li>
    </ul>
    <p class="website">www.meadowlark-cx.example</p>
  </section>

  <!-- Steel set -->
  <section class="card card--front card--steel row-3">
    <div class="emblem-area" role="img" aria-label="Faint brand emblem decoration"></div>
    <h1 class="holder-name">Dana R. Whitcombe</h1>
    <p class="holder-title">Counselor and Life Coach</p>
    <p class="address">47310 County Road 9, Suite 410<br>Plymouth, MN 55490</p>
    <div class="contact-rule"></div>
    <p class="contact-line">Contact -<span class="sep"></span>763-555-0184<span class="sep">-</span>dana@meadowlark-cx.example</p>
  </section>
  <section class="card card--back card--steel row-3">
    <div class="brand">
      <span class="brand-dot"></span>
      <p class="brand-name"><span class="primary">MEADOWLARK</span><span class="secondary">COUNSELING AND COACHING</span></p>
    </div>
    <p class="slogan">Bringing Hope. Transforming Lives.</p>
    <ul class="services">
      <li>Individual counseling</li>
      <li>Relationship counseling</li>
      <li>Group Workshops</li>
      <li>Life Coaching for Teens and Adults</li>
    </ul>
    <p class="website">www.meadowlark-cx.example</p>
  </section>

</body>
</html>
```